Artisan Bread Company Needs a Poster

We need a poster design (with the measurements 1 Ft Horizontal, by 2 Ft Vertical) This poster is to advertise "Hollin's Loaf" and draw attention to the new product. The poster MUST have the "Hollin's Loaf Logo" provided below. (Signage.ai) The lettering below that says "local, organic, sourdough" can be moved around. It must be somewhere on the poster though. The poster is to inform people that the bread is Organic, local, and sourdough.
Feel free to use any pictures that would work.
The poster should have the text-- "Hollin's Loaf is made from 100% Organic flour, grown and milled in Ontario. Hollin's Loaf uses a traditional sourdough method with a long fermentation time, to help with digestibility. All of our breads are hand shaped, and hearth baked in a scorching hot oven."
Target Market(s)
People conscious about their eating habits, anywhere from 24-60. Think yoga moms.
Industry/Entity Type
Bakery
Requirements
Must have
- The poster MUST have the "Hollin's Loaf Logo" provided below. (Signage.ai) The lettering below that says "local, organic, sourdough" can be moved around. It must be somewhere on the poster though. The poster is to inform people that the bread is Organic, local, and sourdough.

```html
<!DOCTYPE html>
<html lang="en">
<head>
<meta charset="utf-8">
<title>Hollin's Loaf – Local Organic Sourdough</title>
<link rel="stylesheet" href="https://fonts.googleapis.com/css2?family=Arimo:ital,wght@0,400;1,400;1,700&display=swap">
<style>
  :root {
    --wood-dark: #2a1710;
    --wood-mid: #442718;
    --wood-light: #5e3b28;
    --flour: rgba(225, 218, 210, 0.42);
    --ribbon: #560a0c;
    --ribbon-shade: #3a0507;
    --ribbon-edge: rgba(255, 255, 255, 0.35);
    --ribbon-text: #f0d7bd;
    --orange-light: #eea12c;
    --orange-deep: #c6690e;
    --ring-yellow: #f1b21c;
    --ring-dots: #e8641c;
    --ink: #3b1a0e;
    --brand-red: #5b0b0d;
    --frame: rgba(255, 255, 255, 0.8);
    --crust-light: #b08556;
    --crust-mid: #7a4e2a;
    --crust-dark: #3e2515;
    --white: #ffffff;
  }
  html, body {
    margin: 0;
    padding: 0;
    width: 1200px;
    height: 2400px;
    overflow: hidden;
    background: var(--wood-dark);
  }
  .poster {
    position: relative;
    width: 1200px;
    height: 2400px;
    overflow: hidden;
    font-family: "Arimo", Arial, sans-serif;
  }
  .wood-background {
    position: absolute;
    inset: 0;
    background:
      radial-gradient(ellipse 380px 520px at 1180px 260px, var(--flour), transparent 72%),
      radial-gradient(ellipse 480px 260px at 0 0, rgba(225,218,210,0.3), transparent 70%),
      radial-gradient(ellipse 260px 800px at 1200px 1150px, rgba(225,218,210,0.28), transparent 70%),
      radial-gradient(ellipse 200px 500px at 0 500px, rgba(225,218,210,0.18), transparent 70%),
      linear-gradient(100deg, var(--wood-dark) 0%, var(--wood-mid) 40%, var(--wood-light) 72%, var(--wood-mid) 100%);
  }
  .frame {
    position: absolute;
    left: 60px;
    top: 58px;
    width: 1080px;
    height: 2300px;
    border: 2px solid var(--frame);
    box-sizing: border-box;
  }
  .brand-name {
    position: absolute;
    top: 240px;
    left: 0;
    width: 1200px;
    text-align: center;
    color: var(--white);
    font-weight: 400;
    font-size: 150px;
    line-height: 180px;
    letter-spacing: 2px;
    margin: 0;
  }
  .graphics {
    position: absolute;
    inset: 0;
  }
  .ribbon-text {
    position: absolute;
    left: 175px;
    top: 584px;
    width: 850px;
    transform: rotate(-5.5deg);
    text-align: center;
    color: var(--ribbon-text);
    font-style: italic;
    font-weight: 400;
    font-size: 34px;
    line-height: 40px;
    letter-spacing: 1px;
    margin: 0;
    white-space: nowrap;
  }
  .ribbon-text .divider { margin: 0 34px; }
  .about {
    position: absolute;
    left: 128px;
    top: 1008px;
    width: 590px;
    padding-left: 28px;
    border-left: 2px solid var(--brand-red);
    color: var(--ink);
    font-style: italic;
    font-size: 33px;
    line-height: 48px;
  }
  .about p { margin: 0 0 14px; }
  .about p:last-child { margin-bottom: 0; }
  .about .brand { font-weight: 700; color: var(--brand-red); }
</style>
</head>
<body>
<main class="poster">
  <div class="wood-background" role="img" aria-label="Dark rustic wooden tabletop dusted with flour"></div>
  <div class="frame"></div>

  <h1 class="brand-name">Hollin's Loaf</h1>

  <svg class="graphics" width="1200" height="2400" viewBox="0 0 1200 2400" xmlns="http://www.w3.org/2000/svg">
    <defs>
      <radialGradient id="orangeFill" cx="0.45" cy="0.35" r="0.7">
        <stop offset="0" stop-color="#eea12c"/>
        <stop offset="1" stop-color="#c6690e"/>
      </radialGradient>
      <linearGradient id="breadFill" x1="0" y1="0" x2="0.25" y2="1">
        <stop offset="0" stop-color="#b08556"/>
        <stop offset="0.35" stop-color="#7a4e2a"/>
        <stop offset="1" stop-color="#3e2515"/>
      </linearGradient>
    </defs>

    <g class="ribbon">
      <polygon points="75,640 215,612 215,688 80,700 130,668" fill="var(--ribbon-shade)"/>
      <polygon points="1133,580 985,560 985,640 1120,650 1080,614" fill="var(--ribbon-shade)"/>
      <polygon points="167,615 1022,538 1030,628 172,705" fill="var(--ribbon)" stroke="var(--ribbon-edge)" stroke-width="1.5"/>
    </g>

    <g class="rings" fill="none">
      <circle cx="440" cy="1340" r="575" stroke="var(--ring-yellow)" stroke-width="3"/>
      <circle cx="440" cy="1340" r="562" stroke="var(--white)" stroke-width="3"/>
      <circle cx="440" cy="1340" r="548" stroke="var(--ring-dots)" stroke-width="4" stroke-dasharray="2 9" stroke-linecap="round"/>
    </g>
    <circle class="info-disc" cx="430" cy="1290" r="490" fill="url(#orangeFill)"/>

    <path class="bread-pile" role="img" aria-label="Pile of rustic flour-dusted sourdough loaves"
      d="M0,1520 C120,1480 260,1490 360,1560 C420,1480 620,1440 780,1445 C860,1450 890,1540 860,1640
         C960,1570 1100,1540 1200,1545 L1200,2400 L0,2400 Z"
      fill="url(#breadFill)"/>
  </svg>

  <p class="ribbon-text">LOCAL<span class="divider">|</span>ORGANIC<span class="divider">|</span>SOURDOUGH</p>

  <section class="about">
    <p><span class="brand">Hollin's Loaf</span> is made from 100% Organic flour, grown and milled in Ontario.</p>
    <p>Hollin's Loaf uses a traditional sourdough method with a long fermentation time, to help with digestibility. All of our breads are hand shaped, and hearth baked in a scorching hot oven.</p>
  </section>
</main>
</body>
</html>
```